Beacon Law Stationary - Law Firm

I am looking for a designer who can help me design letterhead and envelopes consistent with our new business cards. Feel free to reach out to me directly at ned@beaconlawgroup.example. Thank you!! Visit beaconlawgroup.example to see our site and the attached files for creative assets.

Target Market(s)

Anyone needing a lawyer

Font styles to use
Other font styles liked:
• Adobe Caslon Pro

Requirements
Must have
• Adobe Caslon Pro font
Full color
Nice to have
• My photo on front along with 2/3 face of camo - see mock up for example of what I have in mind.

American colors - similar to the ones found on my website and gold.

```html
<!DOCTYPE html>
<html lang="en">
<head>
<meta charset="utf-8">
<title>Beacon Law – Envelope Set</title>
<link rel="stylesheet" href="https://fonts.googleapis.com/css2?family=Libre+Caslon+Text:wght@400;700&display=swap">
<style>
  :root {
    --stage: #a7a8ab;
    --navy: #0f2747;
    --red: #bf1e24;
    --gold: #a48e5a;
    --white: #ffffff;
    --serif: "Libre Caslon Text", "Adobe Caslon Pro", Georgia, serif;
  }
  * { box-sizing: border-box; margin: 0; padding: 0; }
  html, body { width: 1056px; height: 1200px; overflow: hidden; background: var(--stage); }
  .canvas { position: relative; width: 1056px; height: 1200px; font-family: var(--serif); }

  .envelope {
    position: absolute; left: 78px; width: 899px; height: 470px;
    background: var(--white); overflow: hidden;
  }
  .envelope--front { top: 94px; }
  .envelope--back { top: 632px; }
  .envelope__art { position: absolute; inset: 0; }

  .brand { position: absolute; }
  .brand__name {
    font-weight: 700; font-size: 30px; letter-spacing: 1.5px; line-height: 1;
    text-transform: uppercase; color: var(--gold);
  }
  .brand__tagline {
    margin-top: 5px; font-size: 10.5px; color: var(--white);
    text-transform: uppercase; line-height: 1;
  }
  .envelope--front .brand { left: 120px; top: 66px; }
  .envelope--back .brand { left: 166px; top: 63px; }

  .contact {
    position: absolute; left: 634px; top: 22px; font-style: normal;
    color: var(--white); font-size: 12.4px; line-height: 16.4px;
  }
  .contact__address { margin-bottom: 6px; }

  .mission {
    position: absolute; left: 210px; width: 400px; top: 374px;
    text-align: center; color: var(--white); font-weight: 700; font-size: 12px;
    text-transform: uppercase; line-height: 1;
  }
  .badges { position: absolute; left: 356px; top: 404px; display: flex; gap: 18px; align-items: flex-start; }
  .badge-flag { display: flex; flex-direction: column; align-items: center; width: 54px; }
  .badge-flag__shape { width: 37px; height: 23px; background: var(--white); }
  .badge-flag__label { margin-top: 3px; font-size: 7px; line-height: 1; color: var(--white); white-space: nowrap; }
  .badge-seal { width: 33px; height: 33px; border-radius: 50%; background: var(--white); }

  .services {
    position: absolute; left: 212px; top: 443px; line-height: 1;
    color: var(--white); font-size: 12.6px; white-space: nowrap;
  }
  .services .dot { margin: 0 5px; font-size: 9px; vertical-align: 1px; }
</style>
</head>
<body>
<main class="canvas">

  <section class="envelope envelope--front">
    <svg class="envelope__art" width="899" height="470" viewBox="0 0 899 470">
      <defs>
        <linearGradient id="heroFront" x1="0" y1="0" x2="0" y2="1">
          <stop offset="0" stop-color="#eef3f6"/>
          <stop offset="0.55" stop-color="#8a7a5e"/>
          <stop offset="1" stop-color="#1d1c1c"/>
        </linearGradient>
        <linearGradient id="attorneyFront" x1="0" y1="0" x2="0" y2="1">
          <stop offset="0" stop-color="#d8d2cd"/>
          <stop offset="1" stop-color="#2a2b30"/>
        </linearGradient>
      </defs>
      <rect class="band-top" x="0" y="0" width="899" height="131" fill="var(--navy)"/>
      <rect class="band-mission" x="0" y="367" width="899" height="27" fill="var(--red)"/>
      <rect class="band-base" x="0" y="394" width="899" height="76" fill="var(--navy)"/>
      <rect class="photo-hero" x="614" y="131" width="285" height="339" fill="url(#heroFront)" role="img" aria-label="Photo: man with camouflage face paint in a black t-shirt, over soft starburst rays"/>
      <rect class="photo-attorney" x="23" y="236" width="155" height="234" fill="url(#attorneyFront)" role="img" aria-label="Photo: the attorney in a dark suit and blue tie"/>
    </svg>

    <div class="brand">
      <div class="brand__name">Beacon Law</div>
      <div class="brand__tagline">A Veteran Owned Law Firm</div>
    </div>

    <address class="contact">
      <div class="contact__address">450 Harbor Point Avenue Lakemont,<br>Florida 32000</div>
      <div>(555) 010-2480</div>
      <div>avery@beaconlawgroup.example</div>
      <div>beaconlawgroup.example</div>
    </address>

    <div class="mission">Mission: To Fight and Win for You</div>
    <div class="badges">
      <div class="badge-flag"><div class="badge-flag__shape"></div><div class="badge-flag__label">Veteran owned</div></div>
      <div class="badge-seal"></div>
    </div>
    <div class="services">Personal<span class="dot">•</span>Injury<span class="dot">•</span>Injunctions<span class="dot">•</span>Criminal Defense<span class="dot">•</span>Family</div>
  </section>

  <section class="envelope envelope--back">
    <svg class="envelope__art" width="899" height="470" viewBox="0 0 899 470">
      <defs>
        <linearGradient id="heroBack" x1="0" y1="0" x2="0" y2="1">
          <stop offset="0" stop-color="#eef3f6"/>
          <stop offset="0.55" stop-color="#8a7a5e"/>
          <stop offset="1" stop-color="#1d1c1c"/>
        </linearGradient>
        <linearGradient id="attorneyBack" x1="0" y1="0" x2="0" y2="1">
          <stop offset="0" stop-color="#d8d2cd"/>
          <stop offset="1" stop-color="#2a2b30"/>
        </linearGradient>
      </defs>
      <path class="flap" d="M2 0 L899 0 L872 98 Q856 131 826 131 L76 131 Q42 131 30 98 Z" fill="var(--navy)"/>
      <rect class="band-mission" x="0" y="367" width="899" height="27" fill="var(--red)"/>
      <rect class="band-base" x="0" y="394" width="899" height="76" fill="var(--navy)"/>
      <rect class="photo-hero" x="614" y="131" width="285" height="339" fill="url(#heroBack)" role="img" aria-label="Photo: man with camouflage face paint in a black t-shirt, over soft starburst rays"/>
      <rect class="photo-attorney" x="23" y="236" width="155" height="234" fill="url(#attorneyBack)" role="img" aria-label="Photo: the attorney in a dark suit and blue tie"/>
    </svg>

    <div class="brand">
      <div class="brand__name">Beacon Law</div>
      <div class="brand__tagline">A Veteran Owned Law Firm</div>
    </div>

    <div class="mission">Mission: To Fight and Win for You</div>
    <div class="badges">
      <div class="badge-flag"><div class="badge-flag__shape"></div><div class="badge-flag__label">Veteran owned</div></div>
      <div class="badge-seal"></div>
    </div>
    <div class="services">Personal<span class="dot">•</span>Injury<span class="dot">•</span>Injunctions<span class="dot">•</span>Criminal Defense<span class="dot">•</span>Family</div>
  </section>

</main>
</body>
</html>
```